Marwick Ostrand Law website for a law firm

modern clean website for a small boutique law firm. Based in Sacramento, CA and the Bay Area. Practice areas of Family Law, Civil litigation, and Criminal Defense. We already have a logo design as well as attorney pictures to include on page.
Would like images of California included on site.
Would like site to go with Logo that is already designed...blue/grey/white colors.

Industry/Entity Type

Law Firm

Number of Pages Required

5+ page

Requirements
Must have
• I already have several pages of content drafted. Just need the pages with images to input content. Must be clean and modern feel. Want it to reflect California and small boutique feel that is provided personalized legal attention.
• Must have a page where I can blog or post articles on.

```html
<!DOCTYPE html>
<html lang="en">
<head>
<meta charset="utf-8">
<title>Marwick Ostrand Law – Attorney Profile &amp; Practice Areas</title>
<link href="https://fonts.googleapis.com/css2?family=PT+Sans+Narrow:wght@400;700&display=swap" rel="stylesheet">
<style>
  :root {
    --brand-blue: #5b95cf;
    --panel-text: #ffffff;
    --ink: #2a2a2a;
    --page-bg: #ffffff;
  }
  html, body {
    margin: 0;
    padding: 0;
    width: 1200px;
    height: 1125px;
    overflow: hidden;
    background: var(--page-bg);
    font-family: "PT Sans Narrow", "Arial Narrow", sans-serif;
  }
  .page {
    position: relative;
    width: 1200px;
    height: 1125px;
    overflow: hidden;
  }
  .bio-panel {
    position: absolute;
    left: 267px;
    top: 2px;
    width: 667px;
    box-sizing: border-box;
    padding: 18px 19px 17px 19px;
    background: var(--brand-blue);
    border-radius: 5px;
    color: var(--panel-text);
    font-size: 15px;
    line-height: 20px;
  }
  .bio-panel p {
    margin: 0 0 19.5px 0;
  }
  .bio-panel p:last-child { margin-bottom: 0; }
  .practice {
    position: absolute;
    left: 242px;
    top: 712px;
    width: 720px;
    color: var(--ink);
  }
  .practice-title {
    margin: 0;
    text-align: center;
    font-weight: 400;
    font-size: 34px;
    line-height: 44px;
    letter-spacing: 0.2px;
    color: var(--ink);
  }
  .area-title {
    margin: 38px 0 17px 0;
    font-weight: 400;
    font-size: 25px;
    line-height: 30px;
    color: var(--brand-blue);
  }
  .practice p {
    margin: 0 0 19.5px 0;
    font-size: 15px;
    line-height: 20px;
  }
</style>
</head>
<body>
<div class="page">
  <section class="bio-panel">
    <p>Dev Ostrand is a founding partner of Marwick Ostrand Law. After years of helping clients at other local civil litigation law firms, he started this firm so he could serve his clients with the care and devotion they deserve.</p>
    <p>When you are facing a legal issue, it is vital to select a skilled attorney who can understand your situation, and help you secure the most favorable resolution for you. Dev understands the law and is committed to providing the personal attention each client deserves.</p>
    <p>Dev’s practice focuses on general civil litigation, family and immigration law. He has several years of experience helping clients in matters ranging from corporate disputes, fraud, breach of contract, intellectual property theft to employment disputes. Additionally, he helps small and large business with transactional matters, including incorporation of new businesses. He has also helped his clients through difficult times while dealing with a divorce and/or custody battles.</p>
    <p>During his previous positions, Dev has served as insurance defense counsel in complex cases involving personal injuries and damages to real property. He prosecuted criminal matters during his time at the Sacramento District Attorney’s office. His prior experience includes serving as a judicial intern to San Francisco Superior Court Judge, Honorable Helen M. Carver.</p>
    <p>Community Involvement and Interests</p>
    <p>Dev is active in the community and volunteers his time for several local organizations. He has served as a board member of the Capitol Valley Bar Association since 2009; also, served as its President.</p>
    <p>He volunteers his time for the local community ranging from gathering and packaging school supplies to teaching folk dance routines to children.</p>
    <p>He can read, write and fluently speak Punjabi and Hindi.</p>
    <p>Education</p>
    <p>Mr. Ostrand received his J.D. in 2007 from Pacific Delta School of Law, where he also earned an L.L.M. in Transnational Business Practices in 2009.</p>
  </section>

  <section class="practice">
    <h2 class="practice-title">PRACTICE AREAS</h2>
    <h3 class="area-title">Criminal Law</h3>
    <p>If you have been charged with a crime in Northern California, who better to represent you than someone with years of prosecuting experience in the same region? The attorneys at Marwick Ostrand Law know how to get the job done. At Marwick Ostrand Law, we are dedicated to serving our clients in the best possible way. With a strong passion for criminal defense, you can count on Marwick Ostrand Law to fight for your rights and ensure that you receive a fair and just outcome. Years of experience working at various district attorneys’ offices have better prepared our attorneys at Marwick Ostrand Law to defend our clients. Because our team really knows how the prosecuting side thinks and operates, it gives our clients an advantage in pre-trial negotiations.</p>
    <p>With Marwick Ostrand Law, you will have an attorney who is not afraid to go to trial in order to fight for your rights. Having spent years arguing dozens of trials for the prosecution, this law office knows exactly how to get you the verdict you want. Most attorneys do not have the trial experience and work in the back ground of cases. Our attorneys at Marwick Ostrand Law have spent time in actual courtrooms and can use our trial experience to help you.</p>
    <p>The professionals at Marwick Ostrand Law pride themselves on offering our clients the persistence needed to achieve the best results possible. Our firm has the experience needed to understand a wide variety of criminal cases at every stage of the case. We at Marwick Ostrand Law are confident that you will feel secure in our hands, as our top priority is to help you achieve the most favorable results. If you have been charged with a crime, contact our office today.</p>
  </section>
</div>
</body>
</html>
```